Can you make our site AWESOME?

Hi Guys,

I am a co-founder of Tipper Crate Rentals Australia, the world's first e-commerce skip bin business.

We are looking to update our site before a launch into the UK in March.

Please help us by submitting your designs for the following pages:

- Home page (www.tippercraterentals-example.com.au)
- About us (https://www.tippercraterentals-example.com.au/pages/about-us
- Contact us (https://www.tippercraterentals-example.com.au/pages/contact-us)
- Quick Quote / Pricing (https://www.tippercraterentals-example.com.au/pages/free-instant-quote-skip-bin-hire)

NOTES:
- Design should be high-converting
- best designs will be fresh, modern, easy to read, distinctive and memorable
- please use our logo and video colours
- feel free to change logos, layout, images and anything else you feel can be improved
- the winning designer will potentially have the opportunity to re-design the other pages on our site
- brief is for design only

Any questions just ask.

Thanks,
Oliver

```html
<!DOCTYPE html>
<html lang="en">
<head>
<meta charset="utf-8">
<title>Tipper Crate Rentals Australia</title>
<link rel="stylesheet" href="https://fonts.googleapis.com/css2?family=Montserrat:ital,wght@0,400;0,500;0,600;0,700;0,800;1,400;1,500&display=swap">
<style>
:root{
  --green:#34a24c;
  --navy:#2b2d62;
  --ink:#222;
  --grey:#666;
  --light:#f2f2f2;
  --footer:#2a2a2a;
  --star:#f2a93b;
}
*{box-sizing:border-box;margin:0;padding:0}
html,body{width:1200px;height:3577px;overflow:hidden}
body{position:relative;background:#fff;font-family:'Montserrat',sans-serif;color:var(--ink)}
.abs{position:absolute}
a{color:inherit;text-decoration:none}

.topbar{left:0;top:0;width:1200px;height:31px;background:var(--light);font-size:11px;color:#555}
.topbar .call{left:112px;top:9px;display:flex;gap:6px;align-items:center}
.topbar .ship{left:0;width:1200px;top:9px;text-align:center;color:#333;font-weight:500}
.topbar .ship span{color:var(--green)}
.topbar .account{right:109px;top:9px;font-size:10px;color:#777}

.brand{display:flex;align-items:center;gap:10px}
.brand .mark{width:40px;height:30px;background:var(--green)}
.brand .name{font-weight:800;font-size:18px;color:var(--navy);letter-spacing:.5px;line-height:1.1;width:220px}
.header-brand{left:111px;top:50px}

.nav{left:444px;top:60px;display:flex;gap:20px;font-size:12px;color:#333;font-weight:500}
.nav .active{color:var(--green)}
.cart{left:956px;top:59px;font-size:12px;display:flex;gap:6px;align-items:center}
.search{left:1050px;top:57px}

.hero-title{left:0;width:1200px;top:203px;text-align:center;font-size:42px;font-weight:500;letter-spacing:.5px}
.hero-sub{left:0;width:1200px;top:272px;text-align:center;font-size:15px;font-weight:500}
.btn{display:flex;align-items:center;justify-content:center;background:var(--green);color:#fff;font-size:11px;font-weight:500}
.hero-btn{left:519px;top:315px;width:162px;height:39px}
.hero-img{left:0;top:403px;width:1200px;height:330px;background:linear-gradient(90deg,#6fb52d 0%,#2b8fd0 30%,#e98a1e 55%,#e2461c 80%,#f1f1f1 100%)}

.band{left:0;top:0;width:1200px;height:3577px;pointer-events:none}
.cat-title{left:0;width:1200px;top:810px;text-align:center;color:#fff;font-size:29px;font-weight:500}
.cats{left:122px;top:875px;display:flex;gap:20px}
.cat{width:175px;height:171px;background:#fff;display:flex;flex-direction:column;align-items:center;padding-top:30px;gap:22px;font-size:16px;font-weight:600;color:#333}

.section-title{left:0;width:1200px;text-align:center;color:var(--navy);font-weight:700}
.pop-title{top:1166px;font-size:30px}
.products{left:28px;top:1256px;display:flex;gap:19px}
.product{width:271px;text-align:center;font-size:12px;color:#333}
.product .photo{position:relative;height:265px;border:1px solid #ddd;padding:50px 10px}
.product .fill{height:100%;border-radius:6px}
.badge{position:absolute;left:0;top:0;background:var(--green);color:#fff;font-size:12px;padding:3px 10px}
.stars{margin-top:12px;color:var(--star);font-size:10px;letter-spacing:1px}
.stars i{color:#ccc;font-style:normal}
.product .pname{margin-top:8px}
.product .price{margin-top:10px}

.easy-img{left:0;top:1689px;width:603px;height:413px;background:linear-gradient(180deg,#8a8fd6 0%,#aeb3e6 55%,#5ba552 85%,#cfcfcf 100%)}
.easy{left:667px;top:1745px;width:440px;color:#fff}
.easy h2{font-size:31px;font-weight:700}
.easy p.lead{font-size:11px;line-height:17px;margin-top:12px}
.step{display:flex;gap:28px;margin-top:24px}
.step .num{font-size:38px;font-weight:800;width:14px;line-height:38px}
.step h3{font-size:14px;font-weight:700}
.step p{font-size:11px;line-height:17px;margin-top:4px;width:280px}

.review-title{top:2196px;font-size:30px}
.quote-mark{left:0;width:1200px;top:2260px;text-align:center;font-size:34px;color:var(--navy);font-style:italic}
.review{left:262px;width:676px;top:2294px;text-align:center;font-size:15px;line-height:27px;font-style:italic;color:#888}
.reviewer{left:0;width:1200px;top:2421px;text-align:center;font-size:15px;font-weight:500;color:var(--navy)}
.reviewer em{color:var(--green);margin-left:12px}
.arrow{width:32px;height:32px;border:1px solid #ccc;border-radius:50%;top:2320px}

.save-title{top:2584px;color:#fff;font-size:30px}
.feature{top:2672px;width:220px;color:#fff}
.feature h3{margin-top:22px;font-size:16px;font-weight:600;line-height:22px}
.feature p{margin-top:10px;font-size:11px;line-height:19px}

.ready-title{left:109px;top:3004px;font-size:40px;font-weight:800;color:#1f2340}
.ready-sub{left:109px;top:3063px;font-size:20px}
.ready-btn{left:968px;top:3034px;width:124px;height:38px;font-size:13px}

.footer-brand{left:101px;top:3262px}
.footer-brand .name{color:#fff}
.fcol{color:#fff;font-size:13px}
.fcol h4{font-size:12px;font-weight:600;margin-bottom:18px}
.fcol li{list-style:none;margin-bottom:13px}
.finfo{left:110px;top:3318px;color:#fff;font-size:11px;line-height:29px}
.social{left:110px;top:3413px;display:flex;gap:16px}
.social span{width:8px;height:8px;border-radius:50%;background:#fff}
.news p{font-size:10px;line-height:18px;width:300px;margin-bottom:14px}
.news .email{width:230px;height:38px;border:1px solid #fff;padding:10px 14px;font-size:13px}
.news .sub{margin-top:13px;width:124px;height:39px;font-size:13px;font-weight:600}
.pay{left:845px;top:3462px;display:flex;gap:14px}
.pay span{width:34px;height:22px;border-radius:3px;background:#bfbfbf}
.bottombar{left:0;top:3535px;width:1200px;height:42px;background:var(--green);color:#fff;font-size:11px}
.bottombar .copy{left:125px;top:14px}
.bottombar .links{left:751px;top:14px;display:flex;gap:29px}
</style>
</head>
<body>

<div class="abs topbar">
  <div class="abs call"><svg width="12" height="12" viewBox="0 0 24 24"><path d="M6 2l4 4-2 3c1 3 4 6 7 7l3-2 4 4-3 4C10 21 3 14 2 5z" fill="#555"/></svg>CALL NOW: 1800 555 019</div>
  <div class="abs ship">Free Shipping On Orders <span>Over $200</span></div>
  <div class="abs account">Log in &nbsp; or Create account</div>
</div>

<div class="abs brand header-brand"><span class="mark"></span><span class="name">TIPPER CRATE RENTALS AUSTRALIA</span></div>
<nav class="abs nav">
  <a class="active">HOME</a><a>PRICING</a><a>LEARN MORE</a><a>ABOUT</a><a>TRADE SECEERTS</a><a>CONTACT</a>
</nav>
<div class="abs cart">CART <svg width="18" height="16" viewBox="0 0 24 22"><path d="M1 2h4l3 12h12l3-9H7" fill="none" stroke="#333" stroke-width="2"/><circle cx="10" cy="19" r="2" fill="#333"/><circle cx="19" cy="19" r="2" fill="#333"/></svg></div>
<svg class="abs search" width="18" height="18" viewBox="0 0 24 24"><circle cx="10" cy="10" r="7" fill="none" stroke="#222" stroke-width="2.5"/><path d="M15 15l7 7" stroke="#222" stroke-width="2.5"/></svg>

<h1 class="abs hero-title">1000's of Skips at Your Finger Tips</h1>
<p class="abs hero-sub">Best Service &amp; Price | Hassle Free | Australia Wide</p>
<a class="abs btn hero-btn">CALL NOW</a>
<div class="abs hero-img" role="img" aria-label="Row of open skip bins in green, blue, orange and red"></div>

<svg class="abs band" viewBox="0 0 1200 3577">
  <polygon fill="var(--green)" points="132,733 1125,733 1153,787 1200,787 1200,1129 1139,1129 1125,1104 125,1104 104,1129 0,1129 0,787 76,787"/>
  <polygon fill="var(--navy)" points="132,1657 1125,1657 1153,1689 1200,1689 1200,2132 1139,2132 1125,2102 125,2102 104,2132 0,2132 0,1689 76,1689"/>
  <polygon fill="var(--green)" points="132,2531 1125,2531 1153,2563 1200,2563 1200,2934 0,2934 0,2563 76,2563"/>
  <polygon fill="var(--footer)" points="132,3149 1125,3149 1153,3185 1200,3185 1200,3535 0,3535 0,3185 76,3185"/>
</svg>

<h2 class="abs cat-title">SHOP BY CATEGORY</h2>
<div class="abs cats">
  <div class="cat"><svg width="60" height="60" viewBox="0 0 60 60" fill="none" stroke="var(--navy)" stroke-width="2"><rect x="6" y="6" width="24" height="30"/><path d="M11 14h14M11 20h14M11 26h10"/><rect x="32" y="34" width="22" height="20"/><path d="M38 40h4M46 40h4M38 47h4"/></svg>Renovator</div>
  <div class="cat"><svg width="60" height="60" viewBox="0 0 60 60" fill="none" stroke="var(--navy)" stroke-width="2"><circle cx="18" cy="12" r="7"/><circle cx="40" cy="12" r="7"/><path d="M25 12h8M8 30h22l-3 14H11zM34 30h20v24H34zM40 38h8"/></svg>Tradie</div>
  <div class="cat"><svg width="60" height="60" viewBox="0 0 60 60" fill="none" stroke="var(--navy)" stroke-width="2"><path d="M18 22a12 12 0 0 1 24 0zM16 22h28M14 56c0-12 7-20 16-20s16 8 16 20z"/><circle cx="12" cy="36" r="5"/></svg>Builder</div>
  <div class="cat"><svg width="60" height="60" viewBox="0 0 60 60" fill="none" stroke="var(--navy)" stroke-width="2"><path d="M10 30L30 12l20 18M16 26v20h28V26"/><rect x="25" y="34" width="10" height="12"/><path d="M6 40a24 24 0 0 0 48 0"/></svg>Corporate</div>
  <div class="cat"><svg width="60" height="60" viewBox="0 0 60 60" fill="none" stroke="var(--navy)" stroke-width="2"><rect x="18" y="6" width="24" height="48"/><path d="M24 14h12M24 22h12M8 30h10M42 30h10M30 30v16"/><circle cx="30" cy="30" r="4"/></svg>National</div>
</div>

<h2 class="abs section-title pop-title">POPULAR PRODUCT</h2>
<div class="abs products">
  <div class="product"><div class="photo"><div class="fill" role="img" aria-label="Green skip bin" style="background:linear-gradient(180deg,#9bd14a,#6da62a)"></div></div><div class="stars">★★★★<i>★</i></div><div class="pname">SKIP BIN 1</div><div class="price">£120</div></div>
  <div class="product"><div class="photo"><span class="badge">NEW</span><div class="fill" role="img" aria-label="Orange skip bin" style="background:linear-gradient(180deg,#f2622b,#c9400f)"></div></div><div class="stars">★★★★<i>★</i></div><div class="pname">SKIP BIN 1</div><div class="price">£120</div></div>
  <div class="product"><div class="photo"><div class="fill" role="img" aria-label="Green skip bin" style="background:linear-gradient(180deg,#9bd14a,#6da62a)"></div></div><div class="stars">★★★★<i>★</i></div><div class="pname">SKIP BIN 1</div><div class="price">£120</div></div>
  <div class="product"><div class="photo"><span class="badge">NEW</span><div class="fill" role="img" aria-label="Blue skip bin" style="background:linear-gradient(180deg,#3ba6e6,#1f78bf)"></div></div><div class="stars">★★★★<i>★</i></div><div class="pname">SKIP BIN 1</div><div class="price">£120</div></div>
</div>

<div class="abs easy-img" role="img" aria-label="Illustration of a house with a video play button and a thought bubble asking where the skip bin is"></div>
<div class="abs easy">
  <h2>As Easy As 1, 2, 3...</h2>
  <p class="lead">Lorem ipsum dolor sit amet, consectetur adipisicing elit, sed do eius-mod tempor incididunt ut labore et dolore magna aliqua. Ut enim ad</p>
  <div class="step"><span class="num">1</span><div><h3>Simple, Easy Booking</h3><p>Call 1800 555 019 or click here to get started with your instant quote</p></div></div>
  <div class="step"><span class="num">2</span><div><h3>Instant Confirmation</h3><p>Receive your booking details and a 30 minute courtesy call before drop off</p></div></div>
  <div class="step"><span class="num">3</span><div><h3>Gone When Your Ready!</h3><p>Let us know and your bin will be gone within 24hrs</p></div></div>
</div>

<h2 class="abs section-title review-title">Five Star Service</h2>
<div class="abs quote-mark">“</div>
<p class="abs review">The skip bin was delivered earlier that expected on the day of delivery which was excellent. Easy to book through the website and great to have live chat facility- Staff were very friendly and helpful. Cheapest rates I ever seen and would certainly use Tipper Crate Rentals again without a doubt..</p>
<p class="abs reviewer">MARTA K <em>25/04/2018</em></p>
<svg class="abs arrow" style="left:129px" viewBox="0 0 32 32"><path d="M18 10l-6 6 6 6" fill="none" stroke="#bbb" stroke-width="1.5"/></svg>
<svg class="abs arrow" style="left:1039px" viewBox="0 0 32 32"><path d="M14 10l6 6-6 6" fill="none" stroke="#bbb" stroke-width="1.5"/></svg>

<h2 class="abs section-title save-title">Save Time. Save Money.</h2>
<div class="abs feature" style="left:110px"><svg width="48" height="44" viewBox="0 0 48 44" fill="none" stroke="#fff" stroke-width="2"><path d="M4 14l10-8 8 4 10-6 10 8-2 14-8 4-4 10-10-4-10-4z"/></svg><h3>ANY BIN,<br>ANYTIME,ANYWHERE</h3><p>We connect you with local companies Australia wide; for faster response times, less km's and emissions, greater reliability and</p></div>
<div class="abs feature" style="left:358px"><svg width="48" height="44" viewBox="0 0 48 44" fill="none" stroke="#fff" stroke-width="2"><circle cx="24" cy="16" r="10"/><path d="M8 42c2-10 8-14 16-14s14 4 16 14zM12 16a12 12 0 0 1 24 0"/></svg><h3>SERVICE<br>GUARANTEED</h3><p>Want to speak to someone when it suits you? We answer the phones and return calls from 7.30am to 8pm 7 days a</p></div>
<div class="abs feature" style="left:606px"><svg width="48" height="44" viewBox="0 0 48 44" fill="none" stroke="#fff" stroke-width="2"><path d="M18 2h12l-3 8h-6zM16 12h16l4 8v22H12V20z"/><path d="M28 22h-6a3 3 0 0 0 0 6h4a3 3 0 0 1 0 6h-6M24 19v18"/></svg><h3>BEST PRICING</h3><p>We've done the hard work behind the scenes, so with one click you have your best priced, local skip</p></div>
<div class="abs feature" style="left:858px"><svg width="48" height="44" viewBox="0 0 48 44" fill="none" stroke="#fff" stroke-width="2"><path d="M24 2l6 14 15 1-12 10 4 15-13-8-13 8 4-15L3 17l15-1z"/></svg><h3>FIRST CLASS<br>SUPPLY PARTNERS</h3><p>Our local supply partners are the best in the business and share our passion for making you happy.</p></div>

<h2 class="abs ready-title">We're ready to go!</h2>
<p class="abs ready-sub">To book, ask questions or just for a chat, call us 7 days a week, 7.30am to 8pm</p>
<a class="abs btn ready-btn">CALL NOW</a>

<div class="abs brand footer-brand"><span class="mark"></span><span class="name">TIPPER CRATE RENTALS AUSTRALIA</span></div>
<div class="abs finfo">0123 Australia, AU 0987<br>CALL NOW: 1800 555 019<br>info@tippercraterentals-example.com.au</div>
<div class="abs social"><span></span><span></span><span></span><span></span><span></span><span></span></div>

<div class="abs fcol" style="left:386px;top:3254px"><h4>COUNTRY</h4><ul><li>Sydney</li><li>Melbourne</li><li>Brisbane</li><li>Perth</li><li>Adelaide</li><li>Canberra</li></ul></div>
<div class="abs fcol" style="left:599px;top:3254px"><h4>LEARN MORE</h4><ul><li>Waste Types</li><li>Skip Bin Sizes</li><li>Refund Policy</li><li>Pay Later with FlexPay</li><li>FAQ</li><li>Privacy</li></ul></div>
<div class="abs fcol news" style="left:838px;top:3254px"><h4>LATEST INDUSTRY NEWS</h4><p>Sign up for the latest news, offers from TIPPER CRATE RENTALS AUSTRALIA</p><div class="email">Email</div><div class="btn sub">SUBSCRIBE</div></div>
<div class="abs pay"><span></span><span></span><span></span><span></span><span></span></div>

<div class="abs bottombar">
  <div class="abs copy">Copyright © 2019, TIPPER CRATE RENTALS AUSTRALIA. Powered by Storefront</div>
  <div class="abs links"><a>Terms Of Use</a><a>Site map</a><a>Contact</a><a>Privacy Policy</a></div>
</div>

</body>
</html>
```